velmorix - customer deliverable template

Word Template Design for Client Deliverables

We are looking for a professional and polished Word template for our client deliverables, including RFP responses, business proposals, technical proposals, and workshop reports. The template must be fully aligned with our corporate style and branding.

To kick things off, we'll start with our ML Pathfinder Session deliverable document as the base for the new template. This is a very simple project with very limited effort.

Project Resources
All necessary documentation and assets can be found in the following Brenvault Files folder:
https://files.brenvault.example/share/7kQ2wPzrT9xLmA4vBn8cYdE5fHjU3sR?ref=link

The folder includes:
Assets: A folder containing our logos, corporate color palettes, and other design inspiration to help you understand our style.
For additional inspiration, please visit our website: www.velmorix.cloud

Feel free to ask any questions you may have.

Best regards,

Velmorix Team

```html
<!DOCTYPE html>
<html lang="en">
<head>
<meta charset="utf-8">
<title>Velmorix – ML Pathfinder Session Template</title>
<link href="https://fonts.googleapis.com/css2?family=Poppins:wght@400;500;600;700&display=swap" rel="stylesheet">
<style>
  :root {
    --backdrop: #bcbcbc;
    --paper: #ffffff;
    --navy: #0b2a48;
    --navy-deep: #03294a;
    --teal: #0aa39c;
    --ink: #1d1d1f;
    --tab: #d2d2d2;
  }
  * { margin: 0; padding: 0; box-sizing: border-box; }
  html, body { width: 1200px; height: 1123px; overflow: hidden; }
  body {
    background: var(--backdrop);
    font-family: 'Poppins', sans-serif;
    color: var(--ink);
    position: relative;
  }
  .page {
    position: absolute;
    width: 311px;
    height: 441px;
    background: var(--paper);
    overflow: hidden;
  }
  .page > * { position: absolute; }
  .row-top { top: 88px; }
  .row-bottom { top: 592px; }
  .col-1 { left: 100px; }
  .col-2 { left: 448px; }
  .col-3 { left: 793px; }

  /* Covers */
  .cover-dark {
    background:
      radial-gradient(ellipse 70% 22% at 55% 0%, rgba(120, 60, 150, .55), transparent 70%),
      radial-gradient(ellipse 90% 30% at 35% 4%, rgba(10, 163, 156, .45), transparent 70%),
      var(--navy-deep);
  }
  .brand {
    top: 26px; left: 0; width: 100%;
    display: flex; justify-content: center; align-items: center; gap: 5px;
    font-weight: 600; font-size: 21px; color: var(--navy); letter-spacing: -.3px;
  }
  .brand-square { width: 10px; height: 10px; background: var(--teal); }
  .cover-dark .brand { color: #ffffff; }
  .cover-panel { left: 97px; top: 79px; width: 117px; height: 120px; background: var(--teal); }
  .cover-photo {
    left: 94px; top: 175px; width: 124px; height: 124px; border-radius: 50%;
    box-shadow: 0 0 0 5px var(--paper);
  }
  .cover-light .cover-photo { background: radial-gradient(circle at 50% 40%, #e8d2cf, #9b8d90 55%, #1c1c22 90%); }
  .cover-dark .cover-photo {
    background: radial-gradient(circle at 45% 50%, #ff6fd0, #a41d8c 40%, #24124a 80%);
    box-shadow: 0 0 0 5px var(--navy-deep);
  }
  .cover-title { left: 61px; top: 317px; font-weight: 700; font-size: 14px; color: var(--navy); letter-spacing: -.2px; white-space: nowrap; }
  .cover-title span, .section-title span { color: var(--teal); }
  .cover-dark .cover-title { color: #ffffff; }
  .client-meta { left: 61px; top: 354px; font-size: 8.4px; line-height: 11px; color: var(--ink); }
  .client-mark { left: 194px; top: 358px; font-size: 13px; font-weight: 600; color: var(--navy); }
  .cover-rule { left: 61px; top: 381px; width: 189px; height: 1px; background: #9a9a9a; }
  .presented { left: 61px; top: 387px; font-size: 8.4px; color: var(--ink); }
  .cover-dark .client-meta, .cover-dark .presented, .cover-dark .client-mark { color: #ffffff; }
  .cover-dark .cover-rule { background: #7d93a8; }

  /* Shared page parts */
  .mark-square { left: 26px; width: 17px; height: 17px; background: var(--teal); }
  .section-title { left: 26px; font-weight: 700; color: var(--navy); letter-spacing: -.1px; white-space: nowrap; }
  .page-tab { left: 26px; top: 404px; width: 19px; height: 37px; background: var(--tab); }
  .page-num { left: 30px; top: 408px; font-size: 7.5px; color: var(--ink); }
  .page-url { right: 26px; top: 406px; font-size: 8px; color: var(--ink); }

  /* Contents */
  .toc-lead { left: 26px; top: 131px; padding-left: 10px; border-left: 1.5px solid var(--teal); font-size: 10px; line-height: 12.5px; color: var(--navy); }
  .toc-list { left: 26px; top: 168px; width: 260px; list-style: none; }
  .toc-item { display: flex; font-size: 9px; line-height: 11px; color: var(--navy); margin-bottom: 18px; }
  .toc-item .num { width: 24px; font-weight: 600; font-size: 10px; }
  .toc-item .label { flex: 1; }
  .toc-item .pages { width: 30px; text-align: right; }
  .toc-annex { left: 50px; top: 373px; font-size: 9px; font-weight: 600; color: var(--navy); }

  /* Body copy */
  .copy { font-size: 5.1px; line-height: 7.3px; text-align: justify; color: var(--ink); }
  .copy p + p { margin-top: 7px; }
  .sub-head { font-size: 6px; font-weight: 600; color: var(--teal); left: 26px; }
  .strong-note { font-size: 5.2px; font-weight: 600; color: var(--ink); left: 26px; }
  .num-title { left: 26px; top: 36px; font-size: 8px; font-weight: 700; color: var(--navy); white-space: nowrap; }

  .team-photo { bottom: 93px; width: 30px; }
  .team-photo.one { left: 175px; height: 68px; background: linear-gradient(160deg, #c7a48a, #7f5a44); }
  .team-photo.two { left: 215px; height: 88px; background: linear-gradient(160deg, #a9775a, #e9d8c6 60%, #6b4c3b); }
  .team-photo.three { left: 255px; height: 110px; background: linear-gradient(160deg, #8f6b55, #e6ddd6 55%, #b7aa9e); }

  /* Phase diagram */
  .phase-flow { left: 26px; top: 323px; width: 260px; height: 60px; }
  .phase-label { top: 362px; width: 60px; text-align: center; font-size: 5.2px; line-height: 6.4px; }
  .phase-label b { font-weight: 600; }
  .figure-caption { left: 0; width: 100%; top: 386px; text-align: center; font-size: 5.2px; font-weight: 600; }
</style>
</head>
<body>

<!-- Cover, light -->
<section class="page cover-light row-top col-1">
  <div class="brand"><span class="brand-square"></span>velmorix</div>
  <div class="cover-panel"></div>
  <div class="cover-photo" role="img" aria-label="Portrait photo of a person wearing visor glasses with holographic interface rings"></div>
  <h1 class="cover-title">ML PATHFINDER <span>SESSION</span></h1>
  <p class="client-meta">Client Name :<br>Calderon Holdings &nbsp;I&nbsp; 12.09.2025</p>
  <div class="client-mark">Fizzora</div>
  <div class="cover-rule"></div>
  <p class="presented">Presented By : www.velmorix.cloud</p>
</section>

<!-- Cover, dark -->
<section class="page cover-dark row-top col-2">
  <div class="brand"><span class="brand-square"></span>velmorix</div>
  <div class="cover-panel"></div>
  <div class="cover-photo" role="img" aria-label="Neon-lit photo of a person touching a glowing digital interface"></div>
  <h1 class="cover-title">ML PATHFINDER <span>SESSION</span></h1>
  <p class="client-meta">Client Name :<br>Calderon Holdings &nbsp;I&nbsp; 12.09.2025</p>
  <div class="client-mark">Fizzora</div>
  <div class="cover-rule"></div>
  <p class="presented">Presented By : www.velmorix.cloud</p>
</section>

<!-- Contents -->
<section class="page row-top col-3">
  <div class="mark-square" style="top:29px"></div>
  <h2 class="section-title" style="top:66px;font-size:12px">TABLE OF <span>CONTENTS</span></h2>
  <div class="toc-lead">Executive Summary<br>Purpose of this document</div>
  <ol class="toc-list">
    <li class="toc-item"><span class="num">01</span><span class="label">Workshop Overview: The Three<br>Phases of AI Discovery</span><span class="pages">01-02</span></li>
    <li class="toc-item" style="margin-bottom:18px"><span class="num">02</span><span class="label">Discovery Workshop Preparation</span><span class="pages">03-04</span></li>
    <li class="toc-item"><span class="num">03</span><span class="label">Discovery Workshop Session</span><span class="pages">05-06</span></li>
    <li class="toc-item"><span class="num">04</span><span class="label">Next steps</span><span class="pages">07-08</span></li>
  </ol>
  <div class="toc-annex">Annexes</div>
  <div class="page-tab"></div>
  <span class="page-num">01</span>
  <span class="page-url">www.velmorix.cloud</span>
</section>

<!-- Executive summary -->
<section class="page row-bottom col-1">
  <div class="mark-square" style="top:47px"></div>
  <h2 class="section-title" style="top:66px;font-size:10px">EXECUTIVE <span>SUMMARY</span></h2>
  <div class="copy" style="left:26px;top:90px;width:260px">
    <p>In today's dynamic business landscape, Artificial Intelligence stands as a pivotal force for innovation and competitive differentiation. However, many organizations find themselves navigating a complex AI labyrinth, struggling to identify tangible applications and realize a genuine return on investment. The challenge isn't just about understanding AI's theoretical capabilities, but about pinpointing its most impactful and viable applications within your unique operational context.</p>
    <p>At velmorix, we understand that unlocking AI's true potential requires a strategic, well-defined starting point. Our ML Pathfinder Session is meticulously designed to serve as that foundational step. It's a collaborative exploration, guided by our expert team, aimed at demystifying AI and translating its vast possibilities into concrete business value for your organization.</p>
    <p>This report summarizes the key insights and actionable recommendations derived from our joint workshop. It provides you with a clear, prioritized roadmap of the most impactful AI use cases tailored to your business, assessed based on both their potential impact and practical feasibility. Consider this your essential starting point, laying a solid foundation for a successful and strategic AI implementation journey.</p>
  </div>
  <h2 class="section-title" style="top:234px;font-size:10px">PURPOSE OF <span>THIS DOCUMENT</span></h2>
  <div class="copy" style="left:26px;top:262px;width:130px">
    <p>The Purpose of this Document is to provide a comprehensive overview and detailed outcome of the ML Pathfinder Session conducted by velmorix with [Customer Name]. This report serves as a critical deliverable, synthesizing our collaborative efforts to identify, analyze, and prioritize the most impactful and feasible Artificial Intelligence use cases for your business. It is designed to equip your organization with a clear, actionable roadmap, empowering you to make informed decisions and confidently embark on your strategic AI implementation journey.</p>
  </div>
  <div class="team-photo one" role="img" aria-label="Photo of colleagues working together at a table"></div>
  <div class="team-photo two" role="img" aria-label="Photo of a team member smiling during a meeting"></div>
  <div class="team-photo three" role="img" aria-label="Photo of a professional working on a laptop"></div>
  <div class="page-tab"></div>
  <span class="page-num">02</span>
  <span class="page-url">www.velmorix.cloud</span>
</section>

<!-- Workshop overview -->
<section class="page row-bottom col-2">
  <h2 class="num-title">1.&nbsp; WORKSHOP OVERVIEW: THE THREE PHASES OF AI DISCOVERY</h2>
  <div class="copy" style="left:26px;top:57px;width:260px">
    <p>Our ML Pathfinder Session is designed to cut through the complexity of artificial intelligence and pinpoint its most impactful applications for your business. We believe a successful AI journey starts with a clear vision and a structured approach. That's why our workshop is built around three distinct, yet interconnected, phases: Inspire, Discover, and Prioritize. This methodical framework ensures we don't just identify AI possibilities but truly understand their relevance to your operations and map out a viable path to implementation.</p>
  </div>
  <div class="strong-note" style="top:110px">Our Approach: The Three Phases of AI Discovery</div>
  <div class="sub-head" style="top:135px">INSPIRE: IGNITING POSSIBILITIES</div>
  <div class="copy" style="left:26px;top:145px;width:260px">
    <p>In this dynamic 60-minute initial phase, our goal is to inspire you by broadening your perspective on AI's potential. We take you on a journey through various AI approaches, from foundational Artificial Intelligence to groundbreaking AI Agents. With a focus on real-world examples and success stories tailored to your industry, we help you envision a future where AI creates tangible value. This isn't just about understanding the technology; it's about seeing how AI can transform your vision into reality.</p>
  </div>
  <div class="sub-head" style="top:194px">DISCOVER: UNEARTHING CORE OPPORTUNITIES</div>
  <div class="copy" style="left:26px;top:204px;width:260px">
    <p>In this 60-minute collaborative session, our team of experts guides you to uncover core AI use cases unique to your business. We organize you into small groups of three to brainstorm and discuss a wide range of possibilities, from optimizing operations to enhancing customer experiences. With our guidance, each group identifies and select the three most impactful use cases that align with your strategic goals. This hands-on phase transforms potential into a concrete, actionable plan.</p>
  </div>
  <div class="sub-head" style="top:253px">PRIORITIZE: DEFINING YOUR STRATEGIC ROADMAP</div>
  <div class="copy" style="left:26px;top:263px;width:260px">
    <p>During this final 90-minute session, each team presents their top three use cases to the entire group. We then facilitate a collective evaluation, using a robust methodology to rank each idea based on its potential business impact and feasibility of implementation. This process is designed to prioritize the most promising opportunities and ensure your efforts are focused where they deliver the greatest return. The result is not just a list of ideas, but a final list of quick wins you can start implementing right away, giving a clear, actionable roadmap for your AI journey.</p>
  </div>
  <svg class="phase-flow" viewBox="0 0 260 60" aria-label="Three phases joined by arrows: Inspire, Discover, Prioritize">
    <g fill="none" stroke-width="2.5">
      <g transform="translate(28,24)">
        <path d="M-19 -4 A19 19 0 0 1 19 -4" stroke="#a9e0dc"/><circle r="15" stroke="#0aa39c"/>
        <path d="M-5 3 h10 M-3 -4 a4 4 0 1 1 6 0 v3 h-6z" stroke="#1d1d1f" stroke-width="1"/>
      </g>
      <g transform="translate(130,24)">
        <path d="M-19 -4 A19 19 0 0 1 19 -4" stroke="#a9e0dc"/><circle r="15" stroke="#0aa39c"/>
        <circle r="5" stroke="#1d1d1f" stroke-width="1"/><path d="M3.5 3.5 l4 4" stroke="#1d1d1f" stroke-width="1"/>
      </g>
      <g transform="translate(233,24)">
        <path d="M-19 -4 A19 19 0 0 1 19 -4" stroke="#a9e0dc"/><circle r="15" stroke="#0aa39c"/>
        <path d="M-5 5 v-4 M0 5 v-8 M5 5 v-12" stroke="#1d1d1f" stroke-width="1"/>
      </g>
    </g>
    <g stroke="#555" stroke-width=".7" fill="none">
      <path d="M56 24 h46 M99 22 l3 2 -3 2"/>
      <path d="M158 24 h46 M201 22 l3 2 -3 2"/>
    </g>
  </svg>
  <div class="phase-label" style="left:24px"><b>Inspire</b><br>(60 minutes)</div>
  <div class="phase-label" style="left:126px"><b>Discover</b><br>(60 minutes)</div>
  <div class="phase-label" style="left:229px;top:363px"><b>Prioritize</b><br>(90 minutes)</div>
  <div class="figure-caption">Figure 1. The Three Phases of AI Discovery</div>
  <div class="page-tab"></div>
  <span class="page-num">03</span>
  <span class="page-url">www.velmorix.cloud</span>
</section>

<!-- Preparation -->
<section class="page row-bottom col-3">
  <h2 class="num-title">2. DISCOVERY WORKSHOP PREPARATION</h2>
  <div class="copy" style="left:26px;top:57px;width:260px">
    <p>To ensure a productive and truly impactful session, we've designed a meticulous preparation phase tailored to [Customer Name] organization's unique needs. This groundwork is essential for a collaborative environment where every participant can contribute meaningfully, and the outcomes are directly applicable to your business.</p>
  </div>
  <div class="sub-head" style="top:108px">A FOUNDATION OF DIVERSE EXPERTISE</div>
  <div class="copy" style="left:26px;top:118px;width:260px">
    <p>We believe that the best solutions emerge from a variety of perspectives. To that end, we have collaborated with you to identify a diverse group of employees who participated in the workshop. This group included individuals from various roles, functions, and levels of IT expertise. This strategic selection ensures we capture a comprehensive view of your business, from high-level strategic goals to on-the-ground operational realities. A list of these participants is included in Annex 1 for your reference.</p>
  </div>
  <div class="sub-head" style="top:174px">LEVERAGING PARTICIPANT INSIGHTS</div>
  <div class="copy" style="left:26px;top:184px;width:260px">
    <p>Prior to the workshop, each selected participant has been asked to complete a preparatory survey. This detailed questionnaire, which can be found in Annex 2, allows us to gather invaluable insights. We inquired about their specific roles, their expectations for the session, their understanding of the company's strategic goals, and any other relevant information they wish to share. This proactive data collection is a cornerstone of our methodology.</p>
  </div>
  <div class="sub-head" style="top:233px">CUSTOMIZING YOUR WORKSHOP EXPERIENCE</div>
  <div class="copy" style="left:26px;top:243px;width:260px">
    <p>The insights we gain from these surveys allow us to fully customize your workshop. The content, real-world examples, and discussion topics will be precisely adapted to your industry and business context, ensuring the session is immediately relevant and engaging. Furthermore, we will adjust the level of technical vocabulary and the pace of the discussion to match the audience's knowledge level. This is crucial for making the workshop understandable for everyone, preventing participants from getting lost in technical jargon, and ensuring that all voices are heard and valued.</p>
    <p>Our goal is to create an environment where every participant feels empowered to contribute, resulting in a more collaborative and effective outcome for your organization.</p>
  </div>
  <div class="page-tab"></div>
  <span class="page-num">04</span>
  <span class="page-url">www.velmorix.cloud</span>
</section>

</body>
</html>
```